Steelcrest Process Systems. Needs a Business Card Design

We need a business card design for an engineering company which supplies industrial components (pumps, compressors, mechanical seals) provides repairs and services for above mentioned equipments. We offer a uniqe engineering solutions which help our customers to increase the productivness of their manufacturings, and energy savings.

Target Market(s)

Chemical and energy plants, refineries. Food industry and private consumers in a less.

Industry/Entity Type

Business

Contact Information for Business Card

Stylish and sleek design oriented on industrial area.

Requirements
Should not have
• company name shortening

```html
<!DOCTYPE html>
<html lang="en">
<head>
<meta charset="utf-8">
<title>Steelcrest Process Systems – Business Card</title>
<link href="https://fonts.googleapis.com/css2?family=Ubuntu:wght@500&family=PT+Sans:wght@400;700&display=swap" rel="stylesheet">
<style>
  :root {
    --canvas-top: #a9a9a9;
    --canvas-bottom: #6f6f6f;
    --card-dark: #1f1f1f;
    --card-dark-edge: #141414;
    --card-light: #ffffff;
    --ink-dark: #1c1c1c;
    --ink-light: #ffffff;
    --ink-muted: #d2d2d2;
    --accent-orange: #f5a623;
    --accent-red: #e8412c;
    --accent-blue: #2b3f9f;
    --divider: #8a8a8a;
  }
  * { margin: 0; padding: 0; box-sizing: border-box; }
  html, body { width: 1200px; height: 900px; overflow: hidden; }
  body {
    background: linear-gradient(180deg, var(--canvas-top) 0%, var(--canvas-bottom) 100%);
    position: relative;
    font-family: "PT Sans", sans-serif;
  }
  .card {
    position: absolute;
    top: 300px;
    width: 525px;
    height: 300px;
    border-radius: 22px;
    overflow: hidden;
    box-shadow: 0 14px 30px rgba(0,0,0,0.35);
  }
  .card-front {
    left: 50px;
    background: radial-gradient(ellipse at 35% 35%, #2c2c2c 0%, var(--card-dark) 55%, var(--card-dark-edge) 100%);
  }
  .card-back { left: 625px; background: var(--card-dark); }

  .brand-mark {
    display: block;
    border-radius: 50%;
    background: var(--accent-orange);
  }
  .brand-name {
    font-family: "Ubuntu", sans-serif;
    font-weight: 500;
    white-space: nowrap;
  }

  .front-brand {
    position: absolute;
    inset: 0;
    display: flex;
    flex-direction: column;
    align-items: center;
    justify-content: center;
    gap: 26px;
  }
  .front-brand .brand-mark { width: 76px; height: 76px; }
  .front-brand .brand-name { color: var(--ink-light); font-size: 30px; }

  .back-header {
    height: 172px;
    background: var(--card-light);
    display: flex;
    flex-direction: column;
    align-items: center;
    justify-content: flex-end;
    gap: 22px;
    padding-bottom: 18px;
  }
  .back-header .brand-mark { width: 66px; height: 66px; }
  .back-header .brand-name { color: var(--ink-dark); font-size: 27px; }

  .accent-stripe { display: flex; height: 4px; }
  .accent-stripe span:nth-child(1) { flex: 55; background: var(--accent-blue); }
  .accent-stripe span:nth-child(2) { flex: 25; background: var(--accent-orange); }
  .accent-stripe span:nth-child(3) { flex: 20; background: var(--accent-red); }

  .back-details {
    height: 124px;
    background: linear-gradient(180deg, #262626 0%, var(--card-dark) 100%);
    display: flex;
    align-items: center;
    padding-left: 0;
  }
  .person {
    width: 250px;
    text-align: right;
    padding-right: 20px;
  }
  .person-name {
    color: var(--accent-orange);
    font-weight: 700;
    font-size: 19px;
    letter-spacing: 0.3px;
    line-height: 1.1;
  }
  .person-role { color: var(--ink-muted); font-size: 12px; }
  .contact-list {
    list-style: none;
    border-left: 1px solid var(--divider);
    padding: 4px 0 4px 12px;
    color: var(--ink-light);
    font-size: 11.5px;
    line-height: 15px;
  }
  .contact-list li { display: flex; align-items: center; gap: 7px; }
  .contact-list svg { width: 10px; height: 10px; flex: none; }
  .contact-list .no-icon { padding-left: 17px; }
</style>
</head>
<body>

  <section class="card card-front" aria-label="Business card front">
    <div class="front-brand">
      <span class="brand-mark"></span>
      <span class="brand-name">Steelcrest Process Systems</span>
    </div>
  </section>

  <section class="card card-back" aria-label="Business card back">
    <header class="back-header">
      <span class="brand-mark"></span>
      <span class="brand-name">Steelcrest Process Systems</span>
    </header>
    <div class="accent-stripe"><span></span><span></span><span></span></div>
    <div class="back-details">
      <div class="person">
        <p class="person-name">DANA WHITLOCK</p>
        <p class="person-role">Manager</p>
      </div>
      <ul class="contact-list">
        <li>
          <svg viewBox="0 0 10 10"><rect x="2" y="0.5" width="6" height="9" rx="1" fill="#f5a623"/><rect x="3" y="1.8" width="4" height="5" fill="#1f1f1f"/></svg>
          0400 312 987
        </li>
        <li>
          <svg viewBox="0 0 10 10"><path d="M1 4 Q5 0 9 4 L8 5 L6.5 4 L3.5 4 L2 5 Z" fill="#f5a623"/><rect x="2" y="5.5" width="6" height="3.5" rx="0.8" fill="#f5a623"/></svg>
          +61 7 3000 5821
        </li>
        <li>
          <svg viewBox="0 0 10 10"><rect x="0.5" y="2" width="9" height="6.5" rx="0.8" fill="#f5a623"/><path d="M0.8 2.5 L5 5.8 L9.2 2.5" stroke="#1f1f1f" stroke-width="0.9" fill="none"/></svg>
          dana@steelcrestprocess.com
        </li>
        <li>
          <svg viewBox="0 0 10 10"><circle cx="5" cy="5" r="4.2" fill="none" stroke="#f5a623" stroke-width="1"/><ellipse cx="5" cy="5" rx="1.8" ry="4.2" fill="none" stroke="#f5a623" stroke-width="0.8"/><path d="M0.8 5 H9.2" stroke="#f5a623" stroke-width="0.8"/></svg>
          www.steelcrestprocess.com
        </li>
        <li>
          <svg viewBox="0 0 10 10"><path d="M5 0.8 L9.5 5 H8 V9.2 H6 V6.5 H4 V9.2 H2 V5 H0.5 Z" fill="#f5a623"/></svg>
          18 Harlow St Carindale
        </li>
        <li class="no-icon">ABN 51 824 309 617</li>
      </ul>
    </div>
  </section>

</body>
</html>
```